VELMOTIK Amazing Business Cards Challenge

Velmoti is a new technology company that will provide engineering and manufacturing services in the electric vehicle industry.

We are looking at a new business card that will support our orientation in providing advanced, innovative solutions. The business card will be lean and present the only information required to be more efficient.

Target Market(s)

Fleet operators, private commercial vehicle operators, delivery companies.

Industry/Entity Type

Business

Contact Information for Business Card

Use the logo and its colors, use a white background.

Font styles to use
Sans Serif

Colors
0455a3
ffffff
9bcb3c

Requirements
Must have
• Velmotik Logo
• All informations in the DOC file = 3 different cards.
• White background
Nice to have
• Icons for email, phone and web address.
• Cute design and strong identity.
Should not have
• Bleeds

```html
<!DOCTYPE html>
<html lang="en">
<head>
<meta charset="utf-8">
<title>Velmotik business card</title>
<link rel="stylesheet" href="https://fonts.googleapis.com/css2?family=Lato:wght@400;700;900&display=swap">
<style>
  :root {
    --brand-blue: #0455a3;
    --sky-blue: #0b9ad8;
    --accent-green: #9bcb3c;
    --paper: #ffffff;
    --ink: #111418;
    --logo-grey: #5b5d60;
    --stage: #e9e9eb;
  }
  * { box-sizing: border-box; margin: 0; padding: 0; }
  html, body { width: 1200px; height: 905px; overflow: hidden; }
  body {
    background: var(--stage);
    font-family: "Lato", sans-serif;
    position: relative;
  }
  .card {
    position: absolute;
    width: 540px;
    height: 310px;
    top: 298px;
    box-shadow: 0 6px 18px rgba(0,0,0,0.18);
    overflow: hidden;
  }

  /* Front */
  .card-front {
    left: 40px;
    background: linear-gradient(160deg, var(--sky-blue) 0%, var(--brand-blue) 100%);
    display: flex;
    align-items: center;
    justify-content: center;
    gap: 18px;
  }
  .card-front .brand-mark {
    width: 46px; height: 46px;
    background: var(--paper);
  }
  .card-front .brand-name {
    color: var(--paper);
    font-weight: 700;
    font-size: 68px;
    letter-spacing: 1px;
    line-height: 1;
  }

  /* Back */
  .card-back {
    left: 620px;
    background: var(--paper);
  }
  .title-band {
    position: absolute;
    left: 300px; right: 0; top: 34px; height: 40px;
    background: var(--brand-blue);
    color: var(--paper);
    font-size: 13px;
    line-height: 15px;
    text-align: right;
    padding: 5px 14px 0 0;
  }
  .name-band {
    position: absolute;
    left: 0; width: 232px; top: 100px; height: 34px;
    background: var(--brand-blue);
    color: var(--accent-green);
    font-weight: 900;
    font-size: 17px;
    line-height: 34px;
    text-align: right;
    padding-right: 12px;
  }
  .back-mark {
    position: absolute;
    left: 244px; top: 58px;
    width: 52px; height: 52px;
    background: var(--sky-blue);
  }
  .back-brand {
    position: absolute;
    left: 244px; top: 112px;
    color: var(--logo-grey);
    font-weight: 700;
    font-size: 46px;
    line-height: 1;
    letter-spacing: 1px;
  }
  .contact-list {
    position: absolute;
    left: 28px; top: 186px;
    list-style: none;
    font-size: 15px;
    color: var(--ink);
  }
  .contact-list li {
    display: flex; align-items: center; gap: 8px;
    height: 21px;
  }
  .contact-list svg { width: 14px; height: 14px; flex: none; }
  .address {
    position: absolute;
    left: 28px; top: 258px;
    font-size: 15px;
    line-height: 19px;
    color: var(--ink);
  }
</style>
</head>
<body>

<section class="card card-front" aria-label="Card front">
  <span class="brand-mark"></span>
  <span class="brand-name">velmotik</span>
</section>

<section class="card card-back" aria-label="Card back">
  <div class="title-band">V.P. Opérations<br>V.P. Operations</div>
  <div class="name-band">Mathieu Caron</div>
  <span class="back-mark"></span>
  <div class="back-brand">velmotik</div>

  <ul class="contact-list">
    <li>
      <svg viewBox="0 0 16 16" aria-hidden="true"><path fill="#0455a3" d="M3 1.5l2.6 0 1 3.2-1.6 1.2a9 9 0 0 0 5.1 5.1l1.2-1.6 3.2 1v2.6c0 .8-.7 1.5-1.5 1.5C6.6 14.5 1.5 9.4 1.5 3c0-.8.7-1.5 1.5-1.5z"/></svg>
      +1.514.555-0172
    </li>
    <li>
      <svg viewBox="0 0 16 16" aria-hidden="true"><rect x="1" y="3" width="14" height="10" rx="1" fill="#0455a3"/><path d="M1.5 3.8L8 9l6.5-5.2" stroke="#fff" stroke-width="1.3" fill="none"/></svg>
      mcaron@velmotik.com
    </li>
    <li>
      <svg viewBox="0 0 16 16" aria-hidden="true"><circle cx="8" cy="8" r="7" fill="#0455a3"/><path d="M1 8h14M8 1c-3 3.5-3 10.5 0 14M8 1c3 3.5 3 10.5 0 14" stroke="#fff" stroke-width="1" fill="none"/></svg>
      www.velmotik.com
    </li>
  </ul>

  <p class="address">410 – 218 Rue Belvédère Ouest,<br>Montréal (Québec) H3B 2K7 Canada</p>
</section>

</body>
</html>
```